Web-site design for company trading in chemicals & lubricants

We need a standard 5 page web-site designed for our company based in Dubai, UAE.
The web-site should highlight our capacity to store material as well as distribute the same. The products we sell are basic chemicals - packed in bags as well as drums. Bags are big bags - 25 kgs each as well as drums - 200 litres each. We want to highlight the fact that we huge stocks of this material & can deliver by sea & road,
Please use this site as a ref - http://www.norvex-solvents.co.uk/
Besides this, we need a page dedicated to finished products that we are selling for use in the auto industry - lubricants, motor oils,brake-fluids, greases, coolants etc. This are packed in large drums as well as small cans.
It would be nice if the site could immediately also provide a ref. to our location - Dubai or that we are based in the Middle East.
We will provide our company logo for reference

```html
<!DOCTYPE html>
<html lang="en">
<head>
<meta charset="utf-8">
<title>Vantora – Chemicals &amp; Lubricants Trading</title>
<link href="https://fonts.googleapis.com/css2?family=Arimo:wght@400;700&display=swap" rel="stylesheet">
<style>
:root{
  --brown-dark:#4a2512;
  --brown:#5b2f17;
  --brown-mid:#6e3a1d;
  --olive:#7a5c12;
  --gold:#b58d2c;
  --tan:#a98a5e;
  --cream:#f7f1e6;
  --text:#6b6b6b;
  --heading:#7a4a2a;
  --white:#ffffff;
  --nav-text:#3b2a1e;
  --line:#dcdcdc;
}
*{margin:0;padding:0;box-sizing:border-box}
html,body{width:825px;height:1200px;overflow:hidden}
body{position:relative;background:var(--white);font-family:"Arimo",Arial,sans-serif;color:var(--text)}
.abs{position:absolute}

.top-strip{left:0;top:0;width:825px;height:5px;background:var(--brown-dark)}
.header{left:0;top:5px;width:825px;height:96px;background:linear-gradient(#fff,#f4f4f4)}
.brand{display:flex;align-items:center;gap:8px;font-weight:700;color:var(--brown);letter-spacing:1px;white-space:nowrap}
.brand .mark{display:inline-block;background:var(--gold)}
.header-brand{left:43px;top:38px;font-size:30px}
.header-brand .mark{width:12px;height:12px}
.account{left:670px;top:13px;font-size:10px;color:var(--nav-text)}
.phone{left:588px;top:52px;display:flex;align-items:center;gap:10px;font-size:26px;color:var(--brown-dark)}

.nav{left:0;top:101px;width:825px;height:32px;background:linear-gradient(#ffffff,#ececec);border-top:1px solid var(--line);border-bottom:1px solid var(--line)}
.nav ul{list-style:none;position:absolute;left:38px;top:0;display:flex;height:30px}
.nav li{padding:0 12px;line-height:30px;font-size:12px;font-weight:700;color:var(--nav-text);border-right:1px solid var(--line)}
.nav li.active{background:var(--tan);color:var(--white);padding:0 18px}
.search{left:627px;top:108px;width:155px;height:19px;background:var(--white);border:1px solid var(--line);border-radius:3px;font-size:9px;color:#aaa;padding:4px 8px}
.search svg{position:absolute;right:5px;top:3px}

.hero-band{left:0;top:133px;width:825px;height:297px;background:var(--brown)}
.slider{left:38px;top:154px;width:750px;height:239px;border:3px solid #cfcfcf;box-shadow:0 6px 8px rgba(0,0,0,.45);
  background:linear-gradient(180deg,#6fa0cf 0%,#9cc0dd 35%,#b7493b 50%,#2b3d67 72%,#6d7f8a 88%,#3e4f5b 100%)}
.slider .caption{position:absolute;left:12px;top:138px;font-size:27px;line-height:28px;color:var(--white);text-shadow:0 1px 2px rgba(0,0,0,.5)}
.slider .shade{position:absolute;left:0;top:126px;width:330px;height:72px;background:rgba(0,0,0,.25)}
.dots{left:387px;top:408px;display:flex;gap:9px}
.dots span{width:8px;height:8px;border-radius:50%;background:#8b6a55}
.dots span.on{background:#e6e6e6}

.features{left:38px;top:452px;width:750px;height:152px;display:flex}
.feature{position:relative;height:152px;color:var(--white)}
.feature.f1{width:249px;background:var(--brown)}
.feature.f2{width:258px;background:var(--olive)}
.feature.f3{width:243px;background:var(--gold)}
.feature .photo{position:absolute;left:14px;top:20px;width:88px;height:88px;border-radius:50%;border:3px solid var(--white)}
.f1 .photo{background:radial-gradient(circle,#d7643e,#6c1a58)}
.f2 .photo{background:radial-gradient(circle,#f2e6b2,#c99a19)}
.f3 .photo{background:radial-gradient(circle,#f3f1ee,#c7b7a9)}
.feature h3{position:absolute;left:118px;top:14px;font-size:11px;font-weight:700;white-space:nowrap}
.feature p{position:absolute;left:118px;top:34px;width:124px;font-size:9px;line-height:15px}
.btn-more{position:absolute;left:118px;top:117px;height:26px;padding:0 10px;border-radius:3px;font-size:11px;font-weight:700;line-height:26px;color:var(--white)}
.f1 .btn-more{background:var(--tan)}
.f2 .btn-more,.f3 .btn-more{background:#3e2b1a}

.welcome-title{left:43px;top:640px;display:flex;align-items:center;gap:8px;font-size:15px;font-weight:400;color:var(--heading);letter-spacing:1px}
.welcome-title .brand{font-size:21px}
.welcome-title .brand .mark{width:8px;height:8px}
.welcome-text{left:43px;width:504px;font-size:9.1px;line-height:16.4px}
.welcome-text.p1{top:668px}
.welcome-text.p2{top:768px}

.contact{left:571px;top:626px;width:209px;height:296px;background:var(--tan);box-shadow:0 5px 6px rgba(0,0,0,.3)}
.contact h2{position:absolute;left:12px;top:10px;font-size:16px;font-weight:400;color:var(--brown-dark);letter-spacing:1px}
.contact .body{position:absolute;left:0;top:38px;width:209px;height:258px;background:linear-gradient(#b8986a,#a08157)}
.contact label{position:absolute;left:12px;font-size:9.5px;font-weight:700;color:var(--brown-dark)}
.contact .field{position:absolute;left:56px;width:141px;height:18px;background:linear-gradient(#ffffff,var(--cream));border:1px solid #e6d8c2}
.contact .msg{height:67px}
.contact .opt{position:absolute;left:24px;font-size:8px;color:var(--white);display:flex;gap:8px;align-items:center;white-space:nowrap}
.contact .opt span.box{width:10px;height:10px;background:var(--cream);border:1px solid #8a6c44}
.contact .join{position:absolute;left:20px;width:171px;height:27px;border-radius:3px;background:var(--brown-dark);color:#e9d7b8;font-size:11.5px;text-align:center;line-height:27px;letter-spacing:1px;white-space:nowrap}

.partners{left:0;top:950px;width:825px;height:56px;background:linear-gradient(#ffffff,#e9e9e9);border-top:1px solid var(--line)}
.partners .tab{position:absolute;left:59px;top:-1px;width:121px;height:57px;background:var(--white);box-shadow:0 0 6px rgba(0,0,0,.2);font-size:12px;font-weight:700;color:var(--nav-text);text-align:center;line-height:57px}
.partners .badge{position:absolute;top:18px;height:20px;background:#9a9a9a;border-radius:10px}
.partners .badge.round{top:12px;width:34px;height:34px;border-radius:50%;background:#7e8b97}

.footer{left:0;top:1006px;width:825px;height:137px;background:var(--brown-mid)}
.footer ul{position:absolute;top:18px;list-style:none}
.footer li{font-size:9.5px;line-height:18px;color:#e4d3c3;padding-left:12px;position:relative}
.footer li::before{content:"";position:absolute;left:0;top:6px;border-left:4px solid #c7a88c;border-top:3px solid transparent;border-bottom:3px solid transparent}
.footer .info{position:absolute;right:41px;top:24px;text-align:right;font-size:9.5px;line-height:17px;color:#e4d3c3}
.bottom{left:0;top:1143px;width:825px;height:57px;background:var(--brown)}
.bottom .copy{position:absolute;left:43px;top:22px;font-size:9px;color:#b89a80}
.bottom .brand{position:absolute;left:682px;top:19px;font-size:16px;color:var(--white)}
.bottom .brand .mark{width:6px;height:6px;background:#e3cfae}
</style>
</head>
<body>
<div class="abs top-strip"></div>

<header class="abs header"></header>
<div class="abs brand header-brand"><span>VANTORA</span><span class="mark"></span></div>
<div class="abs account">Login &nbsp;/&nbsp; Register</div>
<div class="abs phone">
  <svg width="26" height="26" viewBox="0 0 26 26" aria-hidden="true"><circle cx="13" cy="13" r="12" fill="none" stroke="#4a2512" stroke-width="1.5"/><path d="M9 7c1-1 2-1 2.5 0l1 2c.3.7 0 1.2-.6 1.6-.5.4-.5.9-.2 1.6.6 1.2 1.4 2 2.6 2.6.7.3 1.2.3 1.6-.2.4-.6.9-.9 1.6-.6l2 1c1 .5 1 1.5 0 2.5-1.5 1.5-4 1-6.5-1.5S7.5 8.5 9 7z" fill="#4a2512"/></svg>
  <span>01632 960482</span>
</div>

<nav class="abs nav">
  <ul>
    <li class="active">HOME</li><li>ABOUT</li><li>PRODUCTS</li><li>PARTNERS</li><li>NEWS</li><li style="border-right:0">CONTACT US</li>
  </ul>
</nav>
<div class="abs search">Search
  <svg width="12" height="12" viewBox="0 0 12 12" aria-hidden="true"><circle cx="5" cy="5" r="3.6" fill="none" stroke="#bbb" stroke-width="1.6"/><line x1="7.6" y1="7.6" x2="11" y2="11" stroke="#bbb" stroke-width="1.8"/></svg>
</div>

<section class="abs hero-band"></section>
<div class="abs slider" role="img" aria-label="Cargo ship loaded with shipping containers at a port">
  <div class="shade"></div>
  <div class="caption">Lorem ipsum dolor sit<br>amet, consectetuer</div>
</div>
<div class="abs dots"><span class="on"></span><span></span><span></span><span></span></div>

<section class="abs features">
  <article class="feature f1">
    <div class="photo" role="img" aria-label="Close-up of colourful capsules and tablets"></div>
    <h3>LOREM IPSUM DOLOR</h3>
    <p>Lorem ipsum dolor sit amet, consectetuer adipiscing elit. Aenean commodo ligula eget dolor. Aenean massa.</p>
    <span class="btn-more">LEARN MORE &#9656;</span>
  </article>
  <article class="feature f2">
    <div class="photo" role="img" aria-label="Stacked yellow industrial drums viewed from above"></div>
    <h3>LOREM IPSUM DOLOR</h3>
    <p>Lorem ipsum dolor sit amet, consectetuer adipiscing elit. Aenean commodo ligula eget dolor. Aenean massa.</p>
    <span class="btn-more">LEARN MORE &#9656;</span>
  </article>
  <article class="feature f3">
    <div class="photo" role="img" aria-label="Laboratory scientist examining a sample"></div>
    <h3>LOREM IPSUM DOLOR</h3>
    <p>Lorem ipsum dolor sit amet, consectetuer adipiscing elit. Aenean commodo ligula eget dolor. Aenean massa.</p>
    <span class="btn-more">LEARN MORE &#9656;</span>
  </article>
</section>

<h2 class="abs welcome-title">WELCOME TO <span class="brand"><span>VANTORA</span><span class="mark"></span></span></h2>
<p class="abs welcome-text p1">Lorem ipsum dolor sit amet, consectetuer adipiscing elit. Aenean commodo ligula eget dolor. Aenean massa. Cum sociis natoque penatibus et magnis dis parturient montes, nascetur ridiculus mus. Donec quam felis, ultricies nec, pellentesque eu, pretium quis, sem. Nulla consequat massa quis enim. Donec pede justo, fringilla vel, aliquet nec, vulputate eget, arcu. In enim justo, rhoncus ut, imperdiet a, venenatis vitae, justo. Nullam dictum felis eu pede mollis pretium. Integer tincidunt. Cras dapibus. Vivamus elementum semper nisi. Aenean vulputate eleifend tellus. Aenean leo ligula, porttitor eu,</p>
<p class="abs welcome-text p2">Lorem ipsum dolor sit amet, consectetuer adipiscing elit. Aenean commodo ligula eget dolor. Aenean massa. Cum sociis natoque penatibus et magnis dis parturient montes, nascetur ridiculus mus. Donec quam felis, ultricies nec, pellentesque eu, pretium quis, sem. Nulla consequat massa quis enim. Donec pede justo, fringilla vel, aliquet nec, vulputate eget, arcu. In enim justo, rhoncus ut, imperdiet a, venenatis vitae, justo. Nullam dictum felis eu pede mollis pretium. Integer tincidunt. Cras dapibus. Vivamus elementum semper nisi. Aenean vulputate eleifend tellus. Aenean leo ligula, porttitor eu,</p>

<aside class="abs contact">
  <h2>GET IN TOUCH</h2>
  <div class="body">
    <label style="top:20px">Name:</label><span class="field" style="top:17px"></span>
    <label style="top:49px">Email:</label><span class="field" style="top:46px"></span>
    <label style="top:79px">Phone:</label><span class="field" style="top:76px"></span>
    <label style="top:107px">Message:</label><span class="field msg" style="top:120px"></span>
    <div class="opt" style="top:197px"><span class="box"></span>Please email me news and special offers</div>
    <div class="join" style="top:220px">JOIN OUR MAILING LIST</div>
  </div>
</aside>

<section class="abs partners">
  <div class="tab">OUR PARTNERS</div>
  <span class="badge" style="left:200px;width:38px"></span>
  <span class="badge" style="left:281px;width:38px"></span>
  <span class="badge" style="left:350px;width:38px;border-radius:2px"></span>
  <span class="badge round" style="left:416px"></span>
  <span class="badge" style="left:479px;width:30px"></span>
  <span class="badge" style="left:531px;width:38px"></span>
  <span class="badge" style="left:612px;width:38px"></span>
  <span class="badge" style="left:682px;width:38px;border-radius:2px"></span>
  <span class="badge round" style="left:748px"></span>
</section>

<footer class="abs footer">
  <ul style="left:65px"><li>Home</li><li>About</li><li>Products</li><li>Partners</li><li>News</li><li>Contact Us</li></ul>
  <ul style="left:179px"><li>Home</li><li>About</li><li>Products</li><li>Partners</li><li>News</li><li>Contact Us</li></ul>
  <ul style="left:299px"><li>Home</li><li>About</li><li>Products</li><li>Partners</li><li>News</li><li>Contact Us</li></ul>
  <ul style="left:420px"><li>Home</li><li>About</li><li>Products</li><li>Partners</li><li>News</li><li>Contact Us</li></ul>
  <div class="info">Lorem ipsum dolor sit amet,<br>consectetuer adipiscing elit<br><br>Phone: 01632 960517<br>Fax: 01632 960733<br>Email: info@vantora-trading.com</div>
</footer>
<div class="abs bottom">
  <div class="copy">Copyright © 2011 vantora.com &nbsp;|&nbsp; Terms &amp; Conditions</div>
  <div class="brand"><span>VANTORA</span><span class="mark"></span></div>
</div>
</body>
</html>
```